Stroke Process

I need to create an infographic design that can help me explain the process of a new project that I am working on. The project is a step by step illustration on what needs to be done in order to get a stroke patient that proper wheelchair.

The graphics should walk a client through the process starting with #1 in the inpatient process and the explanation of the steps through the last step in the outpatient process. I uploaded two documents but the document with the explanation is the document to build the illustration on. This is a healthcare piece so the graphics should represent healthcare

```html
<!DOCTYPE html>
<html lang="en">
<head>
<meta charset="utf-8">
<title>Stroke Patient Process</title>
<link rel="stylesheet" href="https://fonts.googleapis.com/css2?family=Oswald:wght@500;600&family=Open+Sans:wght@400;600;700;800&display=swap">
<style>
:root{
  --blue:#3b84c5;
  --blue-dark:#2f6fae;
  --band:#d3e5f5;
  --ink:#1d1d1d;
  --white:#ffffff;
  --frame:#3b84c5;
  --ph-warm:#f0c89a;
}
*{box-sizing:border-box;margin:0;padding:0}
html,body{width:927px;height:1200px;overflow:hidden;background:#fff}
body{font-family:"Open Sans",Arial,sans-serif;color:var(--ink);font-size:12px;line-height:1.3}
.canvas{position:relative;width:927px;height:1200px;border:2px solid var(--frame);overflow:hidden}
.abs{position:absolute}
.title-band{left:0;top:0;width:923px;height:56px;background:var(--blue);color:var(--white);
  font-family:"Oswald",Arial,sans-serif;font-weight:600;font-size:40px;letter-spacing:1px;text-align:center;line-height:56px}
.reason-head{left:12px;top:64px;font-weight:800;color:var(--blue-dark);font-size:16px}
.reason-text{left:12px;top:86px;width:900px;font-size:14px;line-height:1.4}
.band{left:0;top:194px;width:923px;height:26px;background:var(--band)}
.band-label{top:197px;font-weight:800;color:var(--blue-dark);font-size:14px}
.divider{left:463px;top:194px;height:1002px;border-left:2px dashed var(--blue)}
.box{background:var(--blue);color:var(--white);padding:8px 10px;font-size:13px}
.step-head{display:flex;align-items:flex-start;gap:8px;padding-bottom:6px;border-bottom:1px solid rgba(255,255,255,.6);margin-bottom:8px}
.num{flex:none;width:28px;height:30px;background:var(--white);color:var(--ink);font-weight:700;font-size:24px;line-height:30px;text-align:center}
.step-title{font-weight:700;font-size:13.5px;line-height:1.25;padding-top:2px}
.box ul{list-style:none}
.box li{position:relative;padding-left:14px;margin-bottom:3px}
.box li::before{content:"•";position:absolute;left:2px}
.box p{margin-bottom:4px}
.ph{border-radius:4px}
.plain{color:var(--ink)}
.plain h3{font-size:13.5px;font-weight:800;line-height:1.25;margin-bottom:6px}
.plain ul{list-style:none}
.plain li{position:relative;padding-left:14px;margin-bottom:4px}
.plain li::before{content:"•";position:absolute;left:2px}
.plain ol{list-style:none}
.plain ol li::before{content:none}
.plain .sub{padding-left:12px}
.happy{font-weight:800;font-size:13px}
</style>
</head>
<body>
<div class="canvas">
  <div class="abs title-band">STROKE PATIENT PROCESS</div>
  <div class="abs reason-head">REASON FOR FOLLOWING PROCESS RECOMMENDATIONS:</div>
  <p class="abs reason-text">Insurance stroke clients are often discharged before it can be ascertained which mobility equipment will best suit their mobility needs and allow them to perform/participate in their Activities of Daily Living. Yet they require a wheelchair to be discharged. Therefore a rental chair is currently requested which can cause many issues when trying to get Medicare to approve appropriate mobility equipment when specific client issues can be ascertained and documented.</p>

  <div class="abs band"></div>
  <div class="abs band-label" style="left:160px">IN PATIENT PROCESS</div>
  <div class="abs band-label" style="left:600px">OUT PATIENT PROCESS</div>
  <div class="abs divider"></div>

  <section class="abs box" style="left:12px;top:228px;width:224px;height:204px">
    <div class="step-head"><span class="num">1</span><span class="step-title">Patient admitted into Facility With CVA left or right side</span></div>
    <ul>
      <li>46,000 diagnosis in Southern California</li>
      <li>25% Hemiplegia or Hemiparesis</li>
    </ul>
    <div class="abs ph" role="img" aria-label="Hospital building and ambulance illustration" style="left:14px;top:150px;width:130px;height:46px;background:linear-gradient(180deg,#e8f2fb,#b9d6ef)"></div>
  </section>

  <section class="abs box" style="left:12px;top:444px;width:224px;height:136px">
    <div class="step-head" style="border:none;margin-bottom:4px"><span class="num">2</span><span class="step-title">Diagnosed with Hemiplegia or Hemiparesis</span></div>
    <p style="font-size:12.5px">I69.90 Late effects of CVA (Cerebrovascular Accident)<br>I681.90 Hemiplegia<br>I69.354 Hemiparesis</p>
    <div class="abs ph" role="img" aria-label="Medical clipboard icon" style="left:176px;top:84px;width:38px;height:44px;background:#e9f3fb"></div>
  </section>

  <section class="abs box" style="left:12px;top:633px;width:224px;height:553px">
    <div class="step-head" style="border:none;margin-bottom:4px"><span class="num">3</span><span class="step-title">Evaluation</span></div>
    <p>New Language to be used Evaluation with Physical Therapist for functional level. Mobility equipment decision and optimal seating will be based on all the findings from evaluation. Notes from evaluation submitted to therapist which include</p>
    <ul style="margin-top:10px">
      <li>Seating mobility issues to be addressed</li>
      <li>Equipment considered and not chosen with rationale</li>
      <li>Equipment recommended and why client requires each item</li>
      <li>Expected Outcome Reasons for custom power wheelchair vs. transport or standard wheelchair add back benefits of Custom Wheelchair and Manual chair Language</li>
    </ul>
    <div class="abs ph" role="img" aria-label="Patient in hospital bed illustration" style="left:8px;top:500px;width:60px;height:44px;background:#e4eff9"></div>
  </section>

  <section class="abs box" style="left:245px;top:228px;width:210px;height:234px">
    <div class="step-head"><span class="num">4</span><span class="step-title">Prior to Patient Discharge</span></div>
    <ul>
      <li>Mobility Partners Group to bring “loaner” chair</li>
      <li>No charge invoice given to patient</li>
      <li>Transport Chair</li>
      <li>Standard Chair</li>
    </ul>
    <div class="abs ph" role="img" aria-label="Nurse with patient in wheelchair illustration" style="left:150px;top:170px;width:54px;height:58px;background:linear-gradient(180deg,#e6f0fa,#b5d3ee)"></div>
  </section>

  <div class="abs plain" style="left:250px;top:484px;width:210px;font-size:12.5px;line-height:1.3">
    <div style="display:flex;gap:6px"><strong>Send:</strong><span>Mobility Partners Group<br>800.555.0142<br>Face sheet</span></div>
  </div>
  <div class="abs" role="img" aria-label="Medical professional icon" style="left:322px;top:552px;width:62px;height:62px;border-radius:50%;border:2px solid var(--blue);background:#e7f1fa"></div>

  <div class="abs plain" style="left:245px;top:626px;width:214px;font-size:11.4px">
    <h3>Reasons for custom and power wheelchairs vs. transport or stand-ard wheelchair</h3>
    <ul>
      <li><strong style="font-size:13px">Benefits of a Custom Wheelchair</strong></li>
    </ul>
    <div class="sub">
      <p>- K0005 Ultralight weight configurable wheelchair</p>
      <ul style="padding-left:6px">
        <li>Rear Axles can be placed 3” further forward to maximize leverage</li>
        <li>Adjustable posterior tilt of the seat and wheel camber will give better stability for residence ADL’s</li>
      </ul>
    </div>
    <ul><li><strong style="font-size:13px">Benefits of a Power Wheelchair</strong></li></ul>
    <div class="sub">
      <p>- If patient can not propel a smaller base Power Wheel chair is a great solution</p>
      <ul style="padding-left:6px">
        <li>Group 3 PWC is only 24” wide which is 4 inches smaller than a manual wheelchair</li>
        <li>Can be configured with power tilt seat so patient can independently shirt positioning, reducing sitting pressure</li>
      </ul>
    </div>
    <div class="abs ph" role="img" aria-label="Power wheelchair and manual wheelchair icons" style="left:0;top:500px;width:214px;height:52px;background:linear-gradient(90deg,#dbe9f6,#f3f7fb)"></div>
  </div>

  <section class="abs box" style="left:474px;top:228px;width:226px;height:264px;font-size:13px">
    <div style="display:flex;gap:8px"><span class="num">1</span><p>We will measure doorways and look for ingress and egress issues with the residence. Looking for special obstacles such as split level floors, high thresh holds, furniture lay out or uneven exterior pathways. Access issues can cause possible issues with independent mobility and ADL’s</p></div>
  </section>

  <div class="abs plain" style="left:709px;top:234px;width:208px">
    <h3>Important part of the process to determine how patient will use equipment in their own environment</h3>
    <ul style="font-size:10.5px">
      <li>Are there obstacles that need to be removed so patient can operate equipment for ADL’s</li>
      <li>Is a manual chair or power chair better for patient in their home environment</li>
      <li>Measurements for door ways and thresholds</li>
      <li>Community based activities</li>
    </ul>
  </div>

  <section class="abs box" style="left:474px;top:507px;width:226px;height:137px">
    <div class="step-head" style="border:none;margin-bottom:4px"><span class="num">2</span><span class="step-title">Final Out Patient Therapy evaluation</span></div>
    <div class="abs ph" role="img" aria-label="Therapist and patient illustration" style="left:8px;top:54px;width:40px;height:70px;background:#e5eff9"></div>
    <ul style="margin-left:44px;font-size:12px"><li>Evaluation with Physical therapist for final optimal seating and mobility equipment based on all the findings.</li></ul>
  </section>

  <div class="abs plain" style="left:709px;top:510px;width:208px">
    <h3>Notes from evaluation submitted to therapist which include</h3>
    <ol style="font-size:10.5px">
      <li>a)&nbsp; Seating mobility issues to be addressed</li>
      <li>b)&nbsp; Equipment considered and not chosen with rationale</li>
      <li>c)&nbsp; Equipment recommended and why client requires each item</li>
      <li>d)&nbsp; Expected outcome</li>
    </ol>
  </div>

  <section class="abs box" style="left:474px;top:659px;width:226px;height:409px">
    <div class="step-head"><span class="num">3</span><span class="step-title">Completion of final documentation and compliance review</span></div>
    <ul>
      <li>Therapist reviews all notes and combines with PT evaluation to create Letter of Medical Justification</li>
      <li>Letter is signed and submitted to patients MD for patient face to face visit and modifications or con</li>
      <li>All paperwork is submitted for payor approval</li>
      <li>Equipment is ordered</li>
      <li>Equipment is assembled to patient recommended configuration</li>
    </ul>
  </section>

  <div class="abs ph" role="img" aria-label="Caregiver with patient in wheelchair in living room illustration" style="left:709px;top:788px;width:208px;height:257px;background:linear-gradient(180deg,#eaf3fb 0%,#cfe3f4 55%,#f3d3ac 100%)"></div>

  <div class="abs plain" style="left:709px;top:1050px;width:208px">
    <h3>Equipment is delivered, fit and operational training</h3>
    <ul style="font-size:10.5px">
      <li>Review equipment with patient</li>
      <li>Verify that equipment is configured correctly and adjustments made if necessary</li>
      <li class="happy">Happy Patient</li>
    </ul>
  </div>

  <section class="abs box" style="left:474px;top:1091px;width:226px;height:95px">
    <div class="step-head" style="border:none;margin-bottom:2px"><span class="num">4</span><span class="step-title">Delivery of Custom Equipment</span></div>
    <p style="padding-left:36px">Payor final approval</p>
    <div class="abs" role="img" aria-label="Patient avatar icon" style="left:168px;top:44px;width:44px;height:44px;border-radius:50%;background:var(--ph-warm)"></div>
  </section>
</div>
</body>
</html>
```